Building Referrer Relationships Booklet

4 page A4 booklet to give to potential professional referrers to establish a collaborative relationship.Needs to be bright, vibrant, colourful, friendly, inviting, in keeping with The Wren Clinic colours.
Want to provide potential referrer partners a great reason to choose to collaborate with us. They need to know who we are, what makes us different/appealing, and who we are looking for to connect with.
The final product should communicate high performance and connectedness.

Target Market(s)

professional medical allied health and fitness practitioners

Industry/Entity Type

Health

Requirements
Must have
• energetic, vibrant, engaging, inviting, images

```html
<!DOCTYPE html>
<html lang="en">
<head>
<meta charset="utf-8">
<title>Referral Partnerships – The Wren Clinic</title>
<link href="https://fonts.googleapis.com/css2?family=Cormorant+Garamond:wght@500;600&family=Tinos:wght@400;700&display=swap" rel="stylesheet">
<style>
  :root{
    --charcoal:#333333;
    --leaf:#00a651;
    --lime:#a6d046;
    --mint:#cde8d8;
    --teal:#4aa3a8;
    --ink:#231f20;
    --white:#ffffff;
    --rule:#9a9a9a;
  }
  *{box-sizing:border-box;margin:0;padding:0}
  html,body{width:1200px;height:841px;overflow:hidden;background:var(--white)}
  .spread{position:relative;width:1200px;height:841px}

  /* Cover page */
  .cover{position:absolute;left:0;top:0;width:579px;height:841px;background:var(--lime);overflow:hidden;
    font-family:"Cormorant Garamond",serif}
  .cover-curve{position:absolute;left:0;top:0;width:579px;height:360px}
  .cover-title{position:absolute;left:0;width:579px;text-align:center;top:72px;
    font-size:58px;font-weight:500;color:var(--leaf);letter-spacing:.3px;line-height:1}
  .cover-subtitle{position:absolute;left:0;width:579px;text-align:center;top:138px;
    font-size:31px;font-weight:500;color:var(--white);line-height:1}
  .cover-mission{position:absolute;left:0;width:579px;text-align:center;top:195px;
    font-size:29px;font-weight:500;color:var(--white);line-height:35px}
  .cover-photo{position:absolute;left:43px;top:394px;width:506px;height:326px;border-radius:6px;
    background:radial-gradient(ellipse at 50% 50%,rgba(255,255,255,.45),rgba(236,120,150,.18) 45%,rgba(166,208,70,0) 75%)}
  .cover-footer{position:absolute;left:0;top:733px;width:579px;height:108px;background:var(--leaf);
    color:var(--white);text-align:center;font-size:29px;font-weight:500;line-height:36px;padding-top:14px}

  /* About page */
  .about{position:absolute;left:621px;top:0;width:579px;height:841px;border:1px solid var(--rule);border-top:none;
    background:var(--white);font-family:"Tinos",serif;color:var(--ink)}
  .about-header{position:absolute;left:0;top:0;width:100%;height:213px;background:var(--mint)}
  .about-title{position:absolute;left:68px;top:104px;font-family:"Cormorant Garamond",serif;
    font-size:64px;font-weight:500;color:var(--teal);line-height:1}
  .about-photo{position:absolute;left:361px;top:39px;width:165px;height:109px;border:1px solid var(--white);
    background:linear-gradient(135deg,#c9a27a,#8a5a3c 40%,#d9b48f 70%,#f1ece4)}
  .about-values-line{position:absolute;left:62px;top:177px;font-size:17.2px;font-weight:700;letter-spacing:.1px;white-space:nowrap}
  .values{position:absolute;left:94px;top:232px;width:385px}
  .value-name{font-size:17px;font-weight:700;line-height:22px;margin-bottom:8px}
  .value-text{font-size:17px;line-height:21.6px;text-align:justify;margin-bottom:8px}
  .about-footer-bar{position:absolute;left:40px;top:814px;width:491px;height:27px;background:var(--mint)}
</style>
</head>
<body>
<div class="spread">
  <section class="cover">
    <svg class="cover-curve" viewBox="0 0 579 360" aria-hidden="true">
      <path d="M0 0H579V268Q440 352 292 352Q120 352 0 248Z" fill="var(--leaf)"/>
      <path d="M0 0H579V255Q440 340 292 340Q120 340 0 236Z" fill="var(--charcoal)"/>
    </svg>
    <h1 class="cover-title">Referral Partnerships</h1>
    <p class="cover-subtitle">Because Together We Achieve More</p>
    <p class="cover-mission">We are here to help<br>our clients get back on their feet.</p>
    <div class="cover-photo" role="img" aria-label="Photo of four joyful people leaping in the air with arms raised"></div>
    <p class="cover-footer">Let's combine our skillsets so<br>we can achieve even better results</p>
  </section>

  <section class="about">
    <div class="about-header"></div>
    <h2 class="about-title">About Us:</h2>
    <div class="about-photo" role="img" aria-label="Photo of a team stacking their hands together over a wooden floor"></div>
    <p class="about-values-line">COURAGE INSPIRATION FUN CREATIVE WOW TEAM</p>
    <div class="values">
      <h3 class="value-name">COURAGE</h3>
      <p class="value-text">gives us the strength and confidence to take risks and embrace challenges</p>
      <h3 class="value-name">INSPIRATION</h3>
      <p class="value-text">is our energy, our fuel for success, that life force that feeds us as we grow and develop.</p>
      <h3 class="value-name">FUN</h3>
      <p class="value-text">generates happiness, and we all function at our best when we are happy.</p>
      <h3 class="value-name">CREATIVITY</h3>
      <p class="value-text">sets us as an innovative leading-edge business.</p>
      <h3 class="value-name">WOW</h3>
      <p class="value-text">means being the very best we can be and realise our true potential. We are not your average business, our service is not average, and our people are not average.</p>
      <h3 class="value-name">TEAM</h3>
      <p class="value-text" style="text-align:left">and in particular high-performance team means we perform at our very best. Great teamwork creates unity and we accomplish much more than each of us alone.</p>
    </div>
    <div class="about-footer-bar"></div>
  </section>
</div>
</body>
</html>
```